Norwegian language blog www.lumadio.com / www.lumadio.no

I want to make a blog where I share my thoughts and ideas about Norwegian language. I already have a YouTube channel with almost 40000 followers and a podcast with more than 10000 listeners, so this blog will be the extention of those channels. In addition I have my own online school, check www.vilpa.noI have a logo and everything, so I just need a fresh vibrant blog to go with my concept. I want to keep the colors in my logo and also add my logo of course. Then the blog should be easy to read. I need some pictures of the Norwegian flag or something.I want a fun and cool design.
Check my youtube here: https://www.videohub.example/channel/UCxqWPT415mKaZ8Lf2dHoRwn?view_as=subscriber
Website here: www.vilpa.no

The blog will be for my new domain www.lumadio.no and I also have the same domain with www.lumadio.com - I want to put them both in one URL, like when you write www.lumadio.no or .com you will reach the same page.

Target Market(s)

Student who want to learn Norwegian and learn about Norwegian culture

Industry/Entity Type

Education

Coding

Coded - Design and coding required

Number of Pages Required

1 page

Font styles to use
Sans Serif

Colors
e34398
00a990
f78f20
0492cd
86cfc6
85cae6
f8ba93
eda3c7
ffc214

Requirements
Must have
• The colors of my logo, check www.vilpa.no
• Cool and elegant layout
• Pictures of Norway
• Picture of me
• Picture of the Norwegian flag
Should not have
• too many colors and pictures of random people

```html
<!DOCTYPE html>
<html lang="en">
<head>
<meta charset="utf-8">
<title>Lumadio Teaching — Norwegian Language Blog</title>
<link rel="stylesheet" href="https://fonts.googleapis.com/css2?family=Roboto:wght@300;400;500;700;900&family=Lora:wght@400&display=swap">
<style>
:root{
  --red:#e8262d;
  --pink:#ee2250;
  --orange:#e07a18;
  --navy:#002266;
  --white:#ffffff;
  --ink:#111111;
  --teal:#2ab3c8;
  --green:#4cc46a;
  --muted:#8a8a8a;
  --card-text:#444444;
  --soft-red:#ffc4c4;
  --grey-text:#7a7a7a;
}
*{box-sizing:border-box;margin:0;padding:0}
html,body{width:688px;height:1200px;overflow:hidden}
body{position:relative;font-family:'Roboto',sans-serif;background:var(--pink);color:var(--ink)}
.abs{position:absolute}

/* header */
.site-header{left:0;top:0;width:688px;height:41px;background:rgba(130,130,130,.5);border-bottom:1px solid rgba(255,255,255,.25);z-index:3}
.brand{left:91px;top:10px;display:flex;align-items:center;gap:7px;font-weight:300;font-size:11.5px;color:#f0f0f0}
.brand-dot{width:20px;height:20px;border-radius:50%;background:var(--teal)}
.main-nav{left:311px;top:17px;display:flex;gap:16px;font-size:5.3px;letter-spacing:.3px;color:#6a6a6a}
.main-nav .active{color:var(--teal);position:relative}
.main-nav .active::after{content:"";position:absolute;left:-7px;right:-7px;top:18px;height:1px;background:var(--teal)}
.social{left:536px;top:13px;display:flex;gap:3px}
.social span{width:13px;height:13px;border-radius:50%}

/* hero */
.hero{left:0;top:0;width:688px;height:324px;
  background:
    radial-gradient(ellipse 60px 90px at 175px 230px,rgba(150,80,55,.55),transparent),
    radial-gradient(ellipse 70px 60px at 290px 70px,rgba(190,190,190,.35),transparent),
    radial-gradient(ellipse 50px 120px at 280px 250px,rgba(40,40,40,.6),transparent),
    linear-gradient(90deg,#6d6e70 0%,#54575a 14%,#3a3b3d 30%,#4a4744 48%,#393a3c 62%,#5c5f62 82%,#6a6c6f 100%)}
.hero-title{left:130px;top:117px;width:196px;text-align:center;font-weight:900;font-size:17.5px;line-height:22px;color:var(--white);text-shadow:0 0 4px rgba(80,200,220,.7)}
.hero-btn{left:205px;top:197px;width:47px;height:17px;border:1px solid #ddd;border-radius:4px;background:rgba(255,255,255,.18);color:#fff;font-size:5px;font-weight:700;display:flex;align-items:center;justify-content:center}
.hero-media{left:344px;top:101px;width:206px;height:122px;box-shadow:0 0 6px rgba(80,200,220,.8);
  background:
    radial-gradient(ellipse 60px 40px at 45px 75px,rgba(230,210,180,.6),transparent),
    radial-gradient(ellipse 70px 45px at 140px 55px,rgba(220,220,225,.9),transparent),
    linear-gradient(180deg,#4a3a2e 0%,#7a6350 35%,#a58a6c 60%,#cfc6bb 80%,#e8e6e2 100%)}
.media-label{left:377px;top:103px;font-size:14px;font-weight:300;color:#fff}
.media-dot{left:350px;top:106px;width:20px;height:20px;border-radius:50%;background:var(--teal)}

/* flag section */
.flag{left:0;top:324px;width:688px;height:265px;background:var(--red);overflow:hidden}
.flag svg{display:block}
.motto{left:112px;top:415px;font-weight:900;font-size:23.5px;line-height:23.5px;color:var(--ink)}
.motto-rule{left:112px;top:494px;width:155px;height:1px;background:var(--orange)}
.portrait{left:290px;top:373px;width:108px;height:108px;
  background:
    radial-gradient(ellipse 25px 30px at 68px 35px,rgba(200,150,90,.9),transparent),
    radial-gradient(ellipse 35px 25px at 50px 85px,rgba(245,245,245,.95),transparent),
    linear-gradient(180deg,#d6d6d8 0%,#cfcfd1 60%,#3a3a3a 100%)}
.intro{left:279px;top:488px;font-size:5.9px;line-height:8.7px;white-space:nowrap;color:#f2f2f2}
.intro .on-white{color:var(--grey-text)}
.motive{left:434px;top:395px;font-size:5.9px;line-height:8.7px;white-space:nowrap;color:var(--soft-red)}
.motive .on-white{color:#333}
.video{left:434px;top:446px;width:130px;height:72px;
  background:
    radial-gradient(ellipse 22px 30px at 52px 32px,rgba(215,180,130,.9),transparent),
    radial-gradient(ellipse 20px 18px at 88px 38px,rgba(245,240,235,.95),transparent),
    linear-gradient(90deg,#000 0 8%,#8a6a55 20%,#b89a80 45%,#d8d2ca 70%,#000 92%)}

/* join */
.join{left:0;top:589px;width:688px;height:240px;background:linear-gradient(180deg,var(--red),var(--pink))}
.join-title{left:234px;top:643px;width:220px;text-align:center;font-weight:700;font-size:16px;line-height:16.5px;z-index:1}
.join-text{left:214px;top:683px;width:260px;text-align:center;font-size:5.7px;line-height:8.7px;color:#fbd0d4;z-index:1}
.join-btn{left:317px;top:727px;width:54px;height:16px;background:#000;color:#fff;font-size:5.5px;font-weight:700;display:flex;align-items:center;justify-content:center;z-index:1}

/* posts */
.band{left:0;top:0;z-index:0}
.card{width:128px;height:233px;top:837px;background:#fff;z-index:1}
.card-media{position:absolute;left:0;top:0;width:128px;height:127px}
.badge{position:absolute;right:8px;top:7px;padding:1.5px 5px;border-radius:5px;background:var(--green);color:#fff;font-size:4.2px;font-weight:700}
.avatar{position:absolute;left:10px;top:116px;width:22px;height:22px;border-radius:50%;background:#c8c8c8;border:1.5px solid #fff}
.card-title{position:absolute;left:11px;top:143px;font-size:7.6px;font-weight:500;color:#333}
.card-text{position:absolute;left:11px;top:162px;font-size:5px;line-height:7.6px;white-space:nowrap;color:var(--card-text)}
.read-more{position:absolute;left:11px;top:203px;font-size:4.2px;font-weight:700;color:var(--green)}
.card-meta{position:absolute;left:0;top:216px;width:128px;height:17px;border-top:1px solid #eee;padding:5px 11px;font-family:'Lora',serif;font-size:4.2px;color:var(--muted)}

/* footer */
.footer-nav{left:145px;top:1131px;display:flex;gap:11px;font-size:5.8px;color:#f4708f}
.footer-nav .active{color:#000}
.footer-mail{left:440px;top:1131px;width:102px;text-align:right;font-size:5.8px;font-weight:700;color:#fff}
.footer-rule{left:142px;top:1159px;width:404px;height:1px;background:rgba(0,0,0,.12)}
.copyright{left:145px;top:1174px;font-size:4.8px;color:#111}
.footer-icons{left:494px;top:1174px;display:flex;gap:8px}
.footer-icons span{width:6px;height:6px;border-radius:50%;background:#fff}
</style>
</head>
<body>

<section class="abs hero" role="img" aria-label="Photo of a narrow street with white wooden houses in Bergen, darkened"></section>

<header class="abs site-header">
  <div class="abs brand"><span class="brand-dot"></span>Lumadio Teaching</div>
  <nav class="abs main-nav"><span class="active">HOME</span><span>BLOG</span><span>GET IN TOUCH</span></nav>
  <div class="abs social">
    <span style="background:#1da1f2"></span>
    <span style="background:#222"></span>
    <span style="background:#d9252a"></span>
    <span style="background:#3b5998"></span>
  </div>
</header>

<h1 class="abs hero-title">Journey through the Norwegian Language With Me</h1>
<div class="abs hero-btn">Join Me</div>
<div class="abs hero-media" role="img" aria-label="Video still of a laptop showing the school website on a café table"></div>
<span class="abs media-dot"></span>
<div class="abs media-label">Vilpa</div>

<section class="abs flag">
  <svg width="688" height="265" viewBox="0 0 688 265" aria-hidden="true">
    <rect x="188" y="0" width="125" height="265" fill="#fff"/>
    <rect x="0" y="100" width="688" height="125" fill="#fff"/>
    <rect x="219" y="0" width="63" height="265" fill="#002266"/>
    <rect x="0" y="131" width="688" height="63" fill="#002266"/>
  </svg>
</section>

<h2 class="abs motto">Motivation.<br>Passion.<br>Determination.</h2>
<div class="abs motto-rule"></div>
<div class="abs portrait" role="img" aria-label="Portrait photo of the teacher seated, smiling"></div>
<p class="abs intro">Learning another language is such a rewarding<br>experience and will benefit you in every area of your<br>life. Norwegian can be challenging because of the<br><span class="on-white">many rules, exceptions to the rules, and the wide<br>range of dialects spoken in Norway.</span></p>
<p class="abs motive">An important motivation for my teaching is my<br>desire to help students become so comfortable<br>with Norwegian, that they can reliably<br><span class="on-white">communicate their own thoughts and ideas in<br>their new language.</span></p>
<div class="abs video" role="img" aria-label="Video still of the teacher holding a card with the word språk"></div>

<section class="abs join"></section>
<svg class="abs band" width="688" height="1200" viewBox="0 0 688 1200" aria-hidden="true">
  <polygon points="0,802 688,879 688,1106 0,1006" fill="#e07a18"/>
</svg>
<h2 class="abs join-title">Join Me on my Language Adventure</h2>
<p class="abs join-text">There are many variations of passages of Lorem Ipsum available, but the majority have suffered alteration in some form, by injected humour, or randomised words which don't look even slightly believable. If you are going to use a passage of Lorem Ipsum, you need to be sure there isn't anything embarrassing hidden in the middle of text.</p>
<div class="abs join-btn">SIGN UP</div>

<article class="abs card" style="left:142px">
  <div class="card-media" role="img" aria-label="Laptop showing the school website on a café table" style="background:radial-gradient(ellipse 40px 30px at 95px 60px,rgba(220,220,225,.9),transparent),radial-gradient(ellipse 25px 20px at 20px 75px,rgba(225,200,170,.7),transparent),linear-gradient(180deg,#4e4036 0%,#7d6856 40%,#9c9890 70%,#d6d4d0 100%)"></div>
  <span class="badge">UNCATEGORIZED</span>
  <span class="avatar"></span>
  <h3 class="card-title">Example Post 3</h3>
  <p class="card-text">Lorem ipsum dolor sit amet, consectetur<br>adipiscing elit. Duis luctus risus sapien, et<br>varius risus rutrum et. Vestibulum vitae<br>tincidunt velit. Fusce quam libero, pretium</p>
  <span class="read-more">READ MORE »</span>
  <div class="card-meta">December 2, 2018 &nbsp;•&nbsp; No Comments</div>
</article>

<article class="abs card" style="left:280px">
  <div class="card-media" role="img" aria-label="Close-up photo of the teacher" style="background:radial-gradient(ellipse 35px 45px at 64px 55px,rgba(235,200,170,.95),transparent),radial-gradient(ellipse 30px 40px at 64px 125px,rgba(30,30,30,.9),transparent),linear-gradient(90deg,#c9a477 0%,#e3c79c 25%,#d8b88e 75%,#b8915f 100%)"></div>
  <span class="badge">UNCATEGORIZED</span>
  <span class="avatar"></span>
  <h3 class="card-title">Example Post 2</h3>
  <p class="card-text">Lorem ipsum dolor sit amet, consectetur<br>adipiscing elit. Duis luctus risus sapien, et<br>varius risus rutrum et. Vestibulum vitae<br>tincidunt velit. Fusce quam libero, pretium</p>
  <span class="read-more">READ MORE »</span>
  <div class="card-meta">December 2, 2018 &nbsp;•&nbsp; No Comments</div>
</article>

<article class="abs card" style="left:419px">
  <div class="card-media" role="img" aria-label="Photo of the teacher in national costume holding a small Norwegian flag" style="background:radial-gradient(ellipse 22px 30px at 25px 50px,rgba(190,40,50,.75),transparent),radial-gradient(ellipse 28px 40px at 72px 50px,rgba(225,205,165,.9),transparent),radial-gradient(ellipse 45px 30px at 70px 115px,rgba(240,240,240,.95),transparent),linear-gradient(180deg,#8e979c 0%,#a9b0b3 50%,#c9cccc 100%)"></div>
  <span class="badge">UNCATEGORIZED</span>
  <span class="avatar"></span>
  <h3 class="card-title">Example Post 1</h3>
  <p class="card-text">Lorem ipsum dolor sit amet, consectetur<br>adipiscing elit. Duis luctus risus sapien, et<br>varius risus rutrum et. Vestibulum vitae<br>tincidunt velit. Fusce quam libero, pretium</p>
  <span class="read-more">READ MORE »</span>
  <div class="card-meta">December 2, 2018 &nbsp;•&nbsp; No Comments</div>
</article>

<footer>
  <nav class="abs footer-nav"><span class="active">Home</span><span>Blog</span><span>Get In Touch</span></nav>
  <div class="abs footer-mail">contact@lumadio.com</div>
  <div class="abs footer-rule"></div>
  <p class="abs copyright">© 2018 All rights Reserved.</p>
  <div class="abs footer-icons"><span></span><span></span><span></span><span></span></div>
</footer>

</body>
</html>
```